SILVER LANTERN

I need a poster design which is writing the AMBER HARVESTS which I have it
written in my book.The content is spiritual.The poster could be rolled up like a papyrus or a canvas. and could be a wall hanging with tessels and a string to hang. The writing needs to bold and in artistic calligraphy.The background could be starry sky with a light inscription in white GOD IS ONE.The border should be exquisite design in gold. The bottom of the design-border should have seven burgundy red petals.The top could be a dome with an arc of small religious symbols.
The symbols are on the cover of my book

```html
<!DOCTYPE html>
<html lang="en">
<head>
<meta charset="utf-8">
<title>Amber Harvests – God Is One</title>
<link rel="stylesheet" href="https://fonts.googleapis.com/css2?family=Almendra:wght@400;700&family=Lobster+Two:ital,wght@1,700&display=swap">
<style>
  :root {
    --gold-light: #fbe38a;
    --gold: #e0b235;
    --gold-deep: #a8741a;
    --gold-shadow: #6e4a0e;
    --title-gold: #f7b81a;
    --night-deep: #1a0b45;
    --night-violet: #4a1f7a;
    --night-blue: #2a5fc0;
    --beam: #cfe6ff;
    --petal: #e8246a;
    --petal-deep: #a3124a;
    --white: #ffffff;
    --page: #ffffff;
  }
  * { margin: 0; padding: 0; box-sizing: border-box; }
  html, body { width: 849px; height: 1200px; overflow: hidden; background: var(--page); }
  .poster { position: relative; width: 849px; height: 1200px; }
  .frame-art { position: absolute; inset: 0; }
  .panel {
    position: absolute; left: 137px; top: 165px; width: 573px; height: 870px;
    overflow: hidden; text-align: center;
  }
  .title {
    position: absolute; left: 0; right: 0;
    font-family: "Almendra", serif; color: var(--title-gold);
    text-shadow: 2px 3px 3px rgba(40, 10, 60, 0.55);
    line-height: 1;
  }
  .title-main { top: 22px; font-size: 138px; font-weight: 400; letter-spacing: 2px; }
  .title-sub { top: 178px; font-size: 84px; font-weight: 400; letter-spacing: 1px; }
  .proclamation {
    position: absolute; left: 0; right: 0; top: 448px;
    font-family: "Lobster Two", cursive; font-style: italic; font-weight: 700;
    font-size: 68px; color: var(--white); letter-spacing: 2px;
  }
  .attributes {
    position: absolute; left: 0; right: 0; top: 585px;
    font-family: "Lobster Two", cursive; font-style: italic; font-weight: 700;
    font-size: 21px; line-height: 30px; color: var(--white); letter-spacing: 0.3px;
  }
  .attributes span { margin: 0 6px; }
</style>
</head>
<body>
<div class="poster">
  <svg class="frame-art" width="849" height="1200" viewBox="0 0 849 1200" xmlns="http://www.w3.org/2000/svg">
    <defs>
      <linearGradient id="goldFrame" x1="0" y1="0" x2="1" y2="1">
        <stop offset="0" stop-color="var(--gold-light)"/>
        <stop offset="0.3" stop-color="var(--gold)"/>
        <stop offset="0.55" stop-color="var(--gold-deep)"/>
        <stop offset="0.8" stop-color="var(--gold)"/>
        <stop offset="1" stop-color="var(--gold-light)"/>
      </linearGradient>
      <linearGradient id="nightSky" x1="0" y1="0" x2="1" y2="1">
        <stop offset="0" stop-color="var(--night-violet)"/>
        <stop offset="0.35" stop-color="var(--night-blue)"/>
        <stop offset="0.6" stop-color="var(--night-violet)"/>
        <stop offset="1" stop-color="var(--night-deep)"/>
      </linearGradient>
      <linearGradient id="lightBeam" x1="0" y1="0" x2="1" y2="0">
        <stop offset="0" stop-color="var(--beam)" stop-opacity="0"/>
        <stop offset="0.5" stop-color="var(--beam)" stop-opacity="0.75"/>
        <stop offset="1" stop-color="var(--beam)" stop-opacity="0"/>
      </linearGradient>
      <radialGradient id="pinkGlow" cx="0.5" cy="0.5" r="0.5">
        <stop offset="0" stop-color="#ffffff" stop-opacity="0.95"/>
        <stop offset="0.3" stop-color="#f3a6e6" stop-opacity="0.6"/>
        <stop offset="1" stop-color="#c04fc0" stop-opacity="0"/>
      </radialGradient>
      <radialGradient id="starGlow" cx="0.5" cy="0.5" r="0.5">
        <stop offset="0" stop-color="#ffffff"/>
        <stop offset="0.25" stop-color="#ffd0e0" stop-opacity="0.7"/>
        <stop offset="1" stop-color="#ff5080" stop-opacity="0"/>
      </radialGradient>
      <linearGradient id="petalBand" x1="0" y1="0" x2="0" y2="1">
        <stop offset="0" stop-color="var(--petal)"/>
        <stop offset="1" stop-color="var(--petal-deep)"/>
      </linearGradient>
    </defs>

    <g class="gold-frame" role="img" aria-label="Ornate carved gold picture frame with scrollwork corners">
      <rect x="8" y="8" width="833" height="1184" rx="28" fill="url(#goldFrame)"/>
      <rect x="60" y="75" width="729" height="1050" fill="none" stroke="var(--gold-shadow)" stroke-opacity="0.35" stroke-width="3"/>
      <rect x="108" y="135" width="633" height="930" fill="var(--gold-deep)"/>
      <rect x="118" y="146" width="611" height="908" fill="url(#goldFrame)"/>
    </g>

    <g class="night-sky">
      <rect x="137" y="165" width="573" height="870" fill="url(#nightSky)"/>
      <path d="M395 165 C360 380 470 520 410 700 C380 820 300 950 260 1035 L300 1035 C350 940 420 830 445 700 C490 520 410 380 450 165 Z" fill="url(#lightBeam)"/>
      <circle cx="600" cy="290" r="150" fill="url(#pinkGlow)"/>
      <circle cx="633" cy="912" r="55" fill="url(#starGlow)"/>
      <line x1="560" y1="180" x2="700" y2="320" stroke="#ffffff" stroke-opacity="0.25"/>
      <line x1="140" y1="680" x2="330" y2="900" stroke="#ffffff" stroke-opacity="0.2"/>
    </g>

    <rect class="petal-garland" x="140" y="920" width="570" height="110" rx="40" fill="url(#petalBand)" role="img" aria-label="Row of seven deep pink five-petal flowers with leaves"/>
  </svg>

  <div class="panel">
    <h1 class="title title-main">Amber</h1>
    <h2 class="title title-sub">Harvests</h2>
    <p class="proclamation">GOD IS ONE</p>
    <p class="attributes">
      <span>God is Omnioneness</span><span>God is Omnipresent</span><br>
      <span>God is Omnipotent</span><span>God is Omniscient</span><br>
      <span>God is Omnibenevolent</span><span>God is Omniconsciousness</span>
    </p>
  </div>
</div>
</body>
</html>
```